Flyer-Design für Ergotherapie zu Hause
schönes Design, rasche Weiterentwicklung, ist auf meine Wünsche eingegangen, sehr netter und professioneller Kontakt. Vielen Dank für Ihre Arbeit. Alles gute Weiterhin.
Zielgruppe
Ergotherapie zu Hause.
Geriatrie, Neurologie und Handtherapie Klienten
Aufgabenstellung
Es wären auch 3 Flyer möglich mit ähnlichem Design jedoch mit den drei Fachrichtungen Geriatrie, Neurologie und Handtherapie Klienten.
2x3 Seitig gefalzt A4 Quer

```html
<!DOCTYPE html>
<html lang="de">
<head>
<meta charset="utf-8">
<title>Flyer Ergotherapie zu Hause</title>
<link rel="stylesheet" href="https://fonts.googleapis.com/css2?family=Open+Sans:wght@600&family=Roboto:ital,wght@0,300;0,400;0,500;1,300;1,400&display=swap">
<style>
:root{
  --gold:#d09a33;
  --navy:#222e66;
  --stone:#cfccc3;
  --ink:#2b2b2b;
  --frame:#c9c9c9;
  --sepia-dark:#7d6a4e;
  --sepia-mid:#a8916d;
  --sepia-light:#cdbb9b;
  --paper:#ffffff;
}
*{margin:0;padding:0;box-sizing:border-box}
html,body{width:1200px;height:1006px;overflow:hidden;background:var(--paper)}
body{position:relative;font-family:"Roboto",sans-serif;color:var(--ink)}
.page-label{position:absolute;font-size:7px;font-style:italic;font-weight:500;letter-spacing:.3px}
.panel{position:absolute;width:218px;height:463px;overflow:hidden;background:var(--paper);border:1px solid var(--frame)}
.panel.join-left{border-left:1px dashed var(--frame)}
.panel.gold{background:var(--gold)}
.panel>*{position:absolute}
.tab{width:140px;height:140px;border-radius:50%;left:39px;top:-64px;display:flex;align-items:flex-end;justify-content:center;padding-bottom:50px;color:#fff;font-family:"Open Sans",sans-serif;font-weight:600;font-size:15.5px;text-align:center;line-height:1}
.tab.gold{background:var(--gold)}
.tab.navy{background:var(--navy)}
.tab.stone{background:var(--stone);padding-bottom:40px;line-height:1.05}
.dot{width:19px;height:19px;border-radius:50%}
.dot.gold{background:var(--gold)}
.dot.navy{background:var(--navy)}
.dot.stone{background:var(--stone)}
.dot.white{background:#fff}
.copy{left:37px;width:145px;font-size:7.2px;line-height:10px;font-weight:300;text-align:justify}
.copy p+p{margin-top:10px}
.quote{left:36px;width:147px;font-size:7.2px;line-height:9.6px;font-style:italic;font-weight:300;border-top:1.5px dotted var(--ink);border-bottom:1.5px dotted var(--ink);padding:6px 0 5px}
.band{left:0;bottom:0;width:100%;height:7px;background:var(--navy)}
.photo{left:0;width:100%;background:linear-gradient(135deg,var(--sepia-light),var(--sepia-mid) 55%,var(--sepia-dark))}
.caption{right:18px;width:70px;font-size:4.6px;line-height:5.4px;font-style:italic;font-weight:300;color:#f3ead8;text-align:right;border-bottom:1.2px dotted #f3ead8;padding-bottom:4px}
.title{left:0;width:100%;text-align:center;font-weight:400}
.title .main{display:block;font-size:17.5px;color:var(--gold);letter-spacing:.2px}
.title .sub{display:block;font-size:12.2px;font-weight:300;color:#5a6599;letter-spacing:.6px;margin-top:-1px}
.seal{left:39px;top:400px;width:140px;height:140px;border-radius:50%;background:#fff;text-align:center;padding-top:36px}
.seal .mark{display:inline-block;width:12px;height:12px;border-radius:50%;background:var(--navy)}
.seal .name{display:block;margin-top:4px;font-size:12px;letter-spacing:2.6px;color:var(--ink);font-weight:400}
.portrait{left:71px;top:27px;width:75px;height:75px;border-radius:50%;border:4px solid #fff;background:linear-gradient(160deg,#8a8f96,#5d6f7a);}
.rule-w{height:0;border-top:1.2px dotted #fff}
.gold .copy{color:#fff8ea;font-weight:300}
.contact{left:0;width:100%;text-align:center;color:#fff}
.ask{font-size:8.6px;line-height:9.6px;top:306px}
.card{top:336px;font-size:6.3px;line-height:9.2px}
.card b{font-weight:500;display:block;margin-bottom:4px}
.card .gap{display:block;height:6px}
</style>
</head>
<body>

<span class="page-label" style="left:23px;top:11px">Seite 2</span>
<span class="page-label" style="left:241px;top:11px">Seite 3</span>
<span class="page-label" style="left:460px;top:11px">Seite 4</span>
<span class="page-label" style="left:23px;top:512px">Seite 5</span>
<span class="page-label" style="left:241px;top:512px">Seite 6</span>
<span class="page-label" style="left:460px;top:512px">Seite 1</span>

<!-- Innenseite: Seite 2 -->
<section class="panel" style="left:17px;top:27px">
  <div class="tab gold">GERIATRIE</div>
  <div class="dot navy" style="left:99px;top:67px"></div>
  <div class="copy" style="top:102px">
    <p>Aliquip ex ea commodo consequat, puis autem vel eum iriure dolor in hendrerit in vulputate velit esse molestie.</p>
    <p>Consequat, vel illum dolore eu feugiat nulla facilisis at vero eros et accumsan et adipiscing elit, sed diam nonummy nibh iusto odio dignissim qui blandit praesent luptatum zzril delenit augue duis dolore te feugait nulla facilisi erum est.</p>
  </div>
  <div class="dot gold" style="left:99px;top:257px"></div>
  <div class="quote" style="top:296px">Consequat, vel illum dolore eu feugiat nulla facilisis at vero eros et accumsan et iusto odio dignissim qui blandit praesent.</div>
  <div class="copy" style="top:348px">Lorem ipsum dolor sit amet, ipstatem consectetuer adipiscing elit, sed diam nonummy nibh euismod tincidunt laoreet adipiscing elit, sed diam nonummy nibh dolore magna consectetuer adipiscing. Lorem ipsum dolor sit amet, consectetuer adipiscing elit, sed diam nonummy nibh euismod tincidunt laoreet ipstatem.</div>
  <div class="band"></div>
</section>

<!-- Innenseite: Seite 3 -->
<section class="panel join-left" style="left:235px;top:27px">
  <div class="copy" style="top:41px">
    <p>Lorem ipsum dolor sit amet, consectetuer adipiscing elit, sed diam nonummy nibh euismod tincidunt ut laoreet dolore adipiscing elit, sed diam nonummy nibh magna aliquam erat volutpat. Ut wisi enim ad minim veniam, quis nostrud exerci tation ullamcorper suscipit lobortis nisl ut aliquip ex ea commodo consequat. Duis autem vel eum iriure dolor in hendrerit in vulputate velit esse molestie.</p>
    <p>Consequat, vel illum dolore eu feugiat nulla facilisis at vero eros et accumsan et iusto odio dignissim qui blandit praesent luptatum zzril delenit augue duis dolore te feugait nulla facilisi erum est.</p>
  </div>
  <div class="photo" style="top:231px;height:232px" role="img" aria-label="Sepia-Foto: Füsse einer älteren Person neben einem Rollator"></div>
  <div class="caption" style="top:410px">Lorem ipsum dolor sit amet, ad minim veniam, quis nostrud exerci</div>
</section>

<!-- Innenseite: Seite 4 -->
<section class="panel join-left" style="left:453px;top:27px">
  <div class="photo" style="top:0;height:231px" role="img" aria-label="Sepia-Foto: Füsse in Sandalen neben einem Klebeband-Kreuz am Boden"></div>
  <div class="caption" style="top:176px">Lorem ipsum dolor sit amet, ad minim veniam, quis nostrud exerci</div>
  <div class="quote" style="top:266px">Consequat, vel illum dolore eu feugiat nulla facilisis at vero eros et accumsan et iusto odio dignissim qui blandit praesent.</div>
  <div class="copy" style="top:318px">Lorem ipsum dolor sit amet, consectetuer adipiscing elit, sed diam nonummy nibh euismod tincidunt est ut laoreet dolore magna aliquam erat volutpat. Ut wisi enim ad minim veniam, quis nostrud exerci tation ullamcorper suscipit lobortis nisl ut aliquip ex ea commodo consequat. Duis autem vel eum iriure dolor in hendrerit in adipiscing elit, sed diam nonummy nibh vulputate velit esse molestie autem vel eum iriure dolor ullamcorper suscipit.</div>
  <div class="band"></div>
</section>

<!-- Aussenseite: Seite 5 -->
<section class="panel" style="left:17px;top:528px">
  <div class="dot gold" style="left:99px;top:26px"></div>
  <div class="quote" style="top:64px">Consequat, vel illum dolore eu feugiat nulla facilisis at vero eros et accumsan et iusto odio dignissim qui blandit praesent.</div>
  <div class="copy" style="top:115px">Lorem ipsum dolor sit amet, ipstatem consectetuer adipiscing elit, sed diam nonummy nibh euismod tincidunt laoreet adipiscing elit, sed diam nonummy nibh dolore magna consectetuer adipiscing. Lorem ipsum dolor sit amet, consectetuer adipiscing elit, sed diam nonummy nibh euismod tincidunt laoreet ipstatem.</div>
  <div class="photo" style="top:231px;height:232px" role="img" aria-label="Sepia-Foto: Hände beim Einfädeln auf einem Holztisch"></div>
</section>

<!-- Aussenseite: Seite 6 -->
<section class="panel gold join-left" style="left:235px;top:528px">
  <div class="rule-w" style="left:37px;top:64px;width:32px"></div>
  <div class="rule-w" style="left:149px;top:64px;width:32px"></div>
  <div class="portrait" role="img" aria-label="Porträtfoto der Therapeutin"></div>
  <div class="copy" style="top:120px;text-align:justify">Lorem ipsum dolor sit amet, ad minim veniam, quis nostrud exerci tation ullam corper estsuscipit lobortis lorem ipsum exerci tation ullamcorper est ipsum. Corper estsuscipit lobortis lorem ipsum exerci tation ullamcorper est ipsum.</div>
  <div class="rule-w" style="left:37px;top:191px;width:145px"></div>
  <div class="dot white" style="left:99px;top:257px"></div>
  <div class="rule-w" style="left:45px;top:296px;width:128px"></div>
  <div class="contact ask">FÜR WEITERE FRAGEN<br>BIN ICH GERNE FÜR SIE DA</div>
  <div class="rule-w" style="left:45px;top:327px;width:128px"></div>
  <div class="contact card">
    <b>Ergotherapie Halberg</b>
    Sabine Halberg<br>Lindenweg 12<br>8500 Seefeld
    <span class="gap"></span>
    +41 77 000 12 34<br>info@ergotherapie-halberg.ch<br>ergotherapie-halberg@praxis-post.ch
  </div>
  <div class="rule-w" style="left:45px;top:421px;width:128px"></div>
</section>

<!-- Titelseite: Geriatrie -->
<section class="panel join-left" style="left:453px;top:528px">
  <div class="tab gold">GERIATRIE</div>
  <div class="title" style="top:117px"><span class="main">ERGOTHERAPIE</span><span class="sub">BEI IHNEN ZU HAUSE</span></div>
  <div class="dot gold" style="left:99px;top:173px"></div>
  <div class="photo" style="top:231px;height:232px" role="img" aria-label="Sepia-Foto: Hände legen Buchstaben in eine Schale"></div>
  <div class="seal"><span class="mark"></span><span class="name">HALBERG</span></div>
</section>

<!-- Titelseite: Neurologie -->
<section class="panel" style="left:717px;top:528px">
  <div class="tab navy">NEUROLOGIE</div>
  <div class="title" style="top:117px"><span class="main">ERGOTHERAPIE</span><span class="sub">BEI IHNEN ZU HAUSE</span></div>
  <div class="dot navy" style="left:99px;top:172px"></div>
  <div class="photo" style="top:231px;height:232px" role="img" aria-label="Sepia-Foto: Therapeutische Behandlung an der Schulter"></div>
  <div class="seal"><span class="mark"></span><span class="name">HALBERG</span></div>
</section>

<!-- Titelseite: Handtherapie -->
<section class="panel" style="left:957px;top:528px">
  <div class="tab stone">HAND<br>THERAPIE</div>
  <div class="title" style="top:117px"><span class="main">ERGOTHERAPIE</span><span class="sub">BEI IHNEN ZU HAUSE</span></div>
  <div class="dot stone" style="left:99px;top:172px"></div>
  <div class="photo" style="top:231px;height:232px" role="img" aria-label="Sepia-Foto: Hand schreibt eine Einkaufsliste"></div>
  <div class="seal"><span class="mark"></span><span class="name">HALBERG</span></div>
</section>

</body>
</html>
```